Red Kettle Handcrafted Tomato Ketchup packaging design modern

From the best ingredients there is the best ketchup Red Handcrafted ketchup are specially formulated for fine dining and drinks, bringing out all the flavors. As the Red Kettle handcrafted ketchup is otherwise fabulous: Made with wholesome, fully ripe fruits Nothing with half things! All Red Kettle handcrafted ketchups are pure nature, without any artificial diluents or concentrates. Where tomato is on it, that's all there is to it - guaranteed! the design should be professional and noble despite being trendy. A watcher wants to sell the ketchup as merchandising from our restaurant. but as a single brand positioning. The ketchup is vegan. Dimensions: 6.8 cm Height: 7.8 cm Circumference: 21.6 cm The text down (Text 1-4). The lid of the text the glass packaging is black! Thanks for your efforts. I look forward to your designs.

Target Market(s)

foodies

Font styles to use
Serif
Sans Serif

Colors

Designer to choose colors to be used in the design.

Requirements
Must have
• Title: (Handcrafted Tomato Ketchup) Text One: (Store chilled after opening and consume quickly, pasteurized.) Text Two: (Handcrafted in Switzerland by Brentwick Gastro GmbH, Chur www.redkettle-example.ch) Text Tree: (Tomatoes, White Wine Vinegar, Aceto Balsamico, Brown Cane Sugar, Corn Starch, Spices, Salt) Text For: (200 grams) or (200g) The Logo of Red Kettle with the Pasta and Wine have to because of the gesety.
Nice to have
• small vegan icon (maybe)
Should not have
• text of the logo (pasta & wine)

```html
<!DOCTYPE html>
<html lang="de">
<head>
<meta charset="utf-8">
<title>Red Kettle – Handcrafted Tomato Ketchup Label</title>
<link rel="stylesheet" href="https://fonts.googleapis.com/css2?family=Anton&family=Josefin+Sans:wght@400;600&family=Josefin+Slab:wght@600&family=Passion+One&display=swap">
<style>
  :root {
    --ink: #1d1b1b;
    --tomato: #ef4a5a;
    --paper: #ffffff;
    --serif: "Josefin Slab", Georgia, serif;
    --display: "Anton", "Oswald", sans-serif;
    --label: "Passion One", "Arial Black", sans-serif;
    --sans: "Josefin Sans", Arial, sans-serif;
  }
  * { margin: 0; padding: 0; box-sizing: border-box; }
  html, body { width: 1200px; height: 434px; overflow: hidden; background: var(--paper); }
  .label { position: relative; width: 1200px; height: 434px; background: var(--paper); color: var(--ink); }
  .rule { position: absolute; height: 2px; background: var(--ink); }
  .rule--accent { background: var(--tomato); }
  .brand {
    position: absolute; left: 467px; width: 256px; top: 22px; text-align: center;
    font-family: var(--sans); font-weight: 600; font-size: 28px; letter-spacing: 5px; line-height: 1;
  }
  .copy {
    position: absolute; font-family: var(--serif); font-weight: 600;
    font-size: 24px; line-height: 32px; color: var(--ink);
  }
  .copy--care { left: 54px; top: 62px; }
  .copy--origin { left: 54px; top: 232px; }
  .copy--ingredients { left: 832px; top: 153px; }
  .web {
    position: absolute; left: 47px; top: 383px;
    font-family: var(--label); font-size: 22px; letter-spacing: 1.5px; color: var(--tomato);
  }
  .product {
    position: absolute; left: 400px; width: 400px; text-align: center;
    font-family: var(--display); font-size: 84px; line-height: 1; letter-spacing: 1px;
    color: var(--ink); text-shadow: -5px -3px 0 var(--tomato);
  }
  .product--tomato { top: 92px; }
  .product--ketchup { top: 176px; }
  .tagline {
    position: absolute; left: 470px; width: 260px; top: 302px; text-align: center;
    font-family: var(--sans); font-weight: 400; font-size: 24px; letter-spacing: 7px;
  }
  .tomatoes { position: absolute; left: 550px; top: 356px; width: 94px; height: 58px; }
  .title {
    position: absolute; left: 831px; top: 58px;
    font-family: var(--label); font-size: 27px; line-height: 32px; letter-spacing: 1.2px; color: var(--tomato);
  }
  .badge { position: absolute; left: 845px; top: 307px; width: 94px; height: 60px; }
  .net-weight { position: absolute; left: 836px; top: 386px; font-family: var(--serif); font-weight: 600; font-size: 20px; }
  .date-box { position: absolute; left: 985px; top: 301px; width: 188px; height: 103px; border: 1.5px solid var(--ink); }
</style>
</head>
<body>
<main class="label">
  <div class="rule" style="left:0;width:328px;top:35px"></div>
  <div class="rule" style="left:375px;width:92px;top:35px"></div>
  <div class="brand">RED KETTLE</div>
  <div class="rule" style="left:723px;width:94px;top:35px"></div>
  <div class="rule" style="left:866px;width:334px;top:35px"></div>

  <p class="copy copy--care">Nach dem Öffnen gekühlt<br>aufbewahren und rasch<br>konsumieren.<br>Pasteurisiert.</p>
  <div class="rule rule--accent" style="left:54px;width:155px;top:207px"></div>
  <p class="copy copy--origin">Handcrafted in<br>Switzerland by Brentwick<br>Gastro GmbH, Chur</p>
  <p class="web">WWW.REDKETTLE-EXAMPLE.CH</p>

  <h1 class="product product--tomato">TOMATO</h1>
  <div class="product product--ketchup">KETCHUP</div>
  <div class="rule rule--accent" style="left:554px;width:88px;top:275px"></div>
  <p class="tagline">HANDCRAFTED</p>

  <div class="rule" style="left:367px;width:102px;top:397px"></div>
  <div class="rule" style="left:483px;width:26px;top:397px"></div>
  <svg class="tomatoes" viewBox="0 0 94 58" role="img" aria-label="Illustration of two ripe tomatoes">
    <ellipse cx="47" cy="31" rx="45" ry="26" fill="var(--tomato)"/>
  </svg>
  <div class="rule" style="left:695px;width:20px;top:397px"></div>
  <div class="rule" style="left:732px;width:87px;top:397px"></div>

  <h2 class="title">HANDCRAFTED TOMATO<br>KETCHUP</h2>
  <div class="rule rule--accent" style="left:827px;width:154px;top:134px"></div>
  <p class="copy copy--ingredients">Tomaten, Weissweinessig,<br>Aceto Balsamico, brauner<br>Rohrzucker, Maisstärke,<br>Gewürze, Salz</p>

  <svg class="badge" viewBox="0 0 94 60" aria-label="Vegan">
    <path d="M8 30 Q8 6 47 4 Q86 6 86 30 Q86 54 47 56 Q8 54 8 30 Z" fill="none" stroke="var(--ink)" stroke-width="1.6"/>
    <text x="47" y="36" text-anchor="middle" font-family="Passion One, sans-serif" font-size="17" letter-spacing="1" fill="var(--ink)">VEGAN</text>
  </svg>
  <p class="net-weight">200 Gramm</p>
  <div class="date-box"></div>
</main>
</body>
</html>
```